Safety Brochure for Industry Assocations

This is an 8.5 x 11 single sided brochure for our Occupational Health and Safety Data Analytics software. If you need to use stock images we will pay for them.

Please incorporate our logo and some of the images. No need to incorporate them all. We like the idea of the boots being at the bottom of the page but we're open to other ideas.

Please note that we intend to mail this brochure to different industries so it should be generic (i.e. not construction specific).

Target Market(s)

Safety and Industry Organisations for construction, mining, forestry and oil and gas industries.

Industry/Entity Type

Industry

Font styles to use
Sans Serif

Colors

Designer to choose colors to be used in the design.

Requirements
Must have
• We are a software company that produces safety software. Our customers are companies that engage in dangerous work and use our software to improve their worker's safety. The look and feel should convey the fact that:
• -We are Big Data
• -We are Software
• -We service industry
Nice to have
• Please see the Pixfold photo of the boots. We were hoping that the desiger would be able ti modify the image with an overlay of 0's and 1's in a kind of "matrix" fashion to indicate that we are merging traditional labour work with software.
Should not have
• No medical symbols. Note that WE ARE NOT HEALTH CARE.

```html
<!DOCTYPE html>
<html lang="en">
<head>
<meta charset="utf-8">
<title>Safetrend Analytics – Safety Brochure</title>
<link href="https://fonts.googleapis.com/css2?family=Montserrat:wght@400;600;700&family=Roboto+Condensed:wght@400;700&display=swap" rel="stylesheet">
<style>
  :root{
    --green:#3aa935;
    --ink:#333a3d;
    --grey-text:#4a4f52;
    --bar:#c9cccc;
    --orange:#f07a12;
    --dark-band:#2f3334;
  }
  *{margin:0;padding:0;box-sizing:border-box}
  html,body{width:998px;height:1200px;overflow:hidden;background:#fff}
  .brochure{position:relative;width:998px;height:1200px;overflow:hidden;
    background:linear-gradient(180deg,#f4f5f5 0%,#eceeee 55%,#f6f6f6 100%);
    font-family:'Montserrat',sans-serif;color:var(--ink)}
  .hero-photo{position:absolute;left:420px;top:0;width:578px;height:455px;
    background:linear-gradient(90deg,rgba(236,240,244,0) 0%,#c9d8e6 18%,#9db8d4 55%,#7f9dbb 100%)}
  .brand{position:absolute;left:70px;top:50px;display:flex;align-items:center;gap:12px}
  .brand-dot{width:52px;height:52px;border-radius:50%;background:var(--green)}
  .brand-name{font-weight:600;font-size:20px;letter-spacing:3px;color:var(--ink);line-height:1.15}
  .headline{position:absolute;left:58px;top:128px}
  .headline .lead{font-size:30px;font-weight:600;color:var(--ink)}
  .headline .big{font-size:46px;font-weight:700;color:var(--green);line-height:1.1}
  .benefits{position:absolute;left:68px;top:232px;list-style:none;font-size:14px;color:var(--grey-text)}
  .benefits li{position:relative;padding-left:24px;margin-bottom:4px;line-height:1.3}
  .benefits li b{font-weight:700;color:var(--ink)}
  .benefits svg{position:absolute;left:0;top:2px}
  .service-line{position:absolute;left:0;top:458px;width:998px;height:3px;background:var(--green)}
  .service{position:absolute;top:400px;width:250px;text-align:center}
  .service-icon{position:relative;width:112px;height:112px;margin:0 auto;border-radius:50%;
    background:#fff;border:5px solid var(--green);display:flex;align-items:center;justify-content:center}
  .service-num{position:absolute;left:50%;bottom:-14px;transform:translateX(-50%);width:26px;height:26px;
    border-radius:50%;background:var(--orange);color:#fff;font-weight:700;font-size:14px;line-height:26px;border:2px solid #fff}
  .service-title{margin-top:26px;font-weight:700;font-size:17px;letter-spacing:1px;color:var(--ink)}
  .service-items{list-style:none;margin-top:12px}
  .service-items li{background:var(--bar);font-family:'Roboto Condensed',sans-serif;font-size:13px;
    color:#333;height:26px;line-height:26px;margin-bottom:7px}
  .tagline{position:absolute;left:0;width:998px;top:682px;text-align:center}
  .tagline .main{font-family:'Roboto Condensed',sans-serif;font-weight:700;font-size:28px;color:var(--green)}
  .tagline .sub{font-family:'Roboto Condensed',sans-serif;font-weight:700;font-size:27px;color:var(--ink);margin-top:4px}
  .boots-photo{position:absolute;left:70px;top:790px;width:560px;height:270px;
    background:radial-gradient(ellipse at 50% 55%,#6a4a33 0%,#4e3624 45%,rgba(60,45,35,.35) 75%,rgba(240,240,240,0) 100%)}
  .monitor-photo{position:absolute;left:560px;top:770px;width:330px;height:280px;border-radius:8px;
    background:radial-gradient(ellipse at 50% 40%,#f4f5f6 0%,#d9dcde 45%,#3a3d3f 85%,rgba(40,42,44,0) 100%)}
  .contact{position:absolute;left:0;width:998px;top:1085px;text-align:center}
  .phone{display:inline-flex;align-items:center;gap:10px;font-family:'Roboto Condensed',sans-serif;
    font-weight:700;font-size:38px;color:var(--ink)}
  .web{font-size:14px;letter-spacing:8px;color:var(--ink);margin-top:4px}
  .footer-band{position:absolute;left:0;top:1168px;width:998px;height:12px;
    background:linear-gradient(90deg,var(--dark-band) 0 50%,var(--green) 50% 100%)}
</style>
</head>
<body>
<div class="brochure">
  <div class="hero-photo" role="img" aria-label="Photo of business colleagues around a meeting table using phones and tablets, with a glowing data cloud above them"></div>

  <div class="brand">
    <span class="brand-dot"></span>
    <span class="brand-name">SAFETREND<br>Analytics</span>
  </div>

  <div class="headline">
    <div class="lead">Leverage the power</div>
    <div class="big">OF BIG DATA!</div>
  </div>

  <ul class="benefits">
    <li><svg width="15" height="15" viewBox="0 0 16 16"><circle cx="8" cy="8" r="6.5" fill="none" stroke="#3aa935" stroke-width="1.6"/><path d="M5 8.2l2 2 4-4" fill="none" stroke="#3aa935" stroke-width="1.6"/></svg><b>LEAD</b> the next wave of injury reduction</li>
    <li><svg width="15" height="15" viewBox="0 0 16 16"><circle cx="8" cy="8" r="6.5" fill="none" stroke="#3aa935" stroke-width="1.6"/><path d="M5 8.2l2 2 4-4" fill="none" stroke="#3aa935" stroke-width="1.6"/></svg><b>ENGAGE</b> with members through<br>collaboration and benchmarking</li>
    <li><svg width="15" height="15" viewBox="0 0 16 16"><circle cx="8" cy="8" r="6.5" fill="none" stroke="#3aa935" stroke-width="1.6"/><path d="M5 8.2l2 2 4-4" fill="none" stroke="#3aa935" stroke-width="1.6"/></svg><b>PROMOTE</b> standardization</li>
    <li><svg width="15" height="15" viewBox="0 0 16 16"><circle cx="8" cy="8" r="6.5" fill="none" stroke="#3aa935" stroke-width="1.6"/><path d="M5 8.2l2 2 4-4" fill="none" stroke="#3aa935" stroke-width="1.6"/></svg><b>ANALYZE</b> Accurate, Timely and Complete<br>Leading Indicators</li>
    <li><svg width="15" height="15" viewBox="0 0 16 16"><circle cx="8" cy="8" r="6.5" fill="none" stroke="#3aa935" stroke-width="1.6"/><path d="M5 8.2l2 2 4-4" fill="none" stroke="#3aa935" stroke-width="1.6"/></svg><b>TRAIN</b> industry more proactively</li>
  </ul>

  <div class="service-line"></div>

  <section class="service" style="left:90px">
    <div class="service-icon">
      <svg width="62" height="54" viewBox="0 0 62 54" fill="none" stroke="#3aa935" stroke-width="3">
        <rect x="18" y="4" width="40" height="28"/>
        <path d="M38 32v8M30 50l8-10 8 10"/>
        <circle cx="8" cy="10" r="4" fill="#3aa935" stroke="none"/>
        <path d="M8 16v22M8 20l12 -6"/>
      </svg>
      <span class="service-num">1</span>
    </div>
    <h2 class="service-title">TRAINING</h2>
    <ul class="service-items">
      <li>Analyze needs of Industry</li>
      <li>Deliver Proactive Training</li>
      <li>Improve Safety</li>
    </ul>
  </section>

  <section class="service" style="left:374px">
    <div class="service-icon">
      <svg width="60" height="60" viewBox="0 0 60 60" fill="none" stroke="#3aa935" stroke-width="5" stroke-linecap="round">
        <path d="M12 48L40 20"/>
        <circle cx="44" cy="16" r="8" stroke-width="4"/>
        <path d="M16 12l32 36" stroke-width="6"/>
        <path d="M10 8l6 4"/>
      </svg>
      <span class="service-num">2</span>
    </div>
    <h2 class="service-title">BENCHMARKING</h2>
    <ul class="service-items">
      <li>Engage with Members</li>
      <li>Promote Collaborative Advancement of Safety</li>
      <li>Improve Safety</li>
    </ul>
  </section>

  <section class="service" style="left:658px">
    <div class="service-icon">
      <svg width="62" height="62" viewBox="0 0 62 62" fill="none" stroke="#3aa935" stroke-width="2">
        <circle cx="31" cy="31" r="7"/>
        <g fill="#3aa935" stroke="none">
          <circle cx="31" cy="7" r="3.5"/><circle cx="31" cy="55" r="3.5"/>
          <circle cx="10" cy="19" r="3.5"/><circle cx="52" cy="19" r="3.5"/>
          <circle cx="10" cy="43" r="3.5"/><circle cx="52" cy="43" r="3.5"/>
        </g>
        <path d="M31 7v17M31 38v17M10 19l15 8M52 19l-15 8M10 43l15-8M52 43l-15-8M31 7L52 19 52 43 31 55 10 43 10 19Z" stroke-dasharray="3 3"/>
      </svg>
      <span class="service-num">3</span>
    </div>
    <h2 class="service-title">TREND ANALYSIS</h2>
    <ul class="service-items">
      <li>Monitor Industry Trends</li>
      <li>Implement Corrective Initiatives</li>
      <li>Improve Safety</li>
    </ul>
  </section>

  <div class="tagline">
    <div class="main">THE NEXT BIG STEP IN INJURY REDUCTION!</div>
    <div class="sub">For your entire industry</div>
  </div>

  <div class="boots-photo" role="img" aria-label="Photo of worn leather work boots standing in soil, overlaid with a matrix of digits"></div>

  <div class="monitor-photo" role="img" aria-label="Product screenshot on a desktop monitor showing a training expiry report"></div>

  <div class="contact">
    <div class="phone">
      <svg width="32" height="32" viewBox="0 0 24 24"><path d="M6.6 10.8a15.1 15.1 0 0 0 6.6 6.6l2.2-2.2c.3-.3.7-.4 1-.2 1.1.4 2.3.6 3.6.6.6 0 1 .4 1 1V20c0 .6-.4 1-1 1A17 17 0 0 1 3 4c0-.6.4-1 1-1h3.5c.6 0 1 .4 1 1 0 1.3.2 2.5.6 3.6.1.3 0 .7-.2 1z" fill="#3aa935"/></svg>
      1-888-555-0142
    </div>
    <div class="web">WWW.SAFETRENDANALYTICS.COM</div>
  </div>

  <div class="footer-band"></div>
</div>
</body>
</html>
```